Illustration Design Project

I have an existing illustration I have written up, I need it professionally redone, perhaps as an infographic or new design from the current layout.

Pls plan for a few edits and revisions.

I will need it large enough to be made into a wall poster size.

```html
<!DOCTYPE html>
<html lang="en">
<head>
<meta charset="utf-8">
<title>Accountable / Victim Ladder</title>
<link href="https://fonts.googleapis.com/css2?family=Montserrat:wght@800&family=Roboto:wght@400;700;900&display=swap" rel="stylesheet">
<style>
  :root {
    --bg: #ffffff;
    --column: #333333;
    --column-dark: #2a2a2a;
    --step: #e6e6e6;
    --step-number: #2e2e2e;
    --band-from: #2f6fb8;
    --band-to: #62a8e2;
    --arc: #3b7ec6;
    --arc-light: #6bb0e6;
    --yellow: #f2e600;
    --magenta: #e0218a;
    --green: #9ccc2e;
    --blue: #5db3e8;
    --purple: #9a80d6;
    --quote: #ffffff;
  }
  * { box-sizing: border-box; margin: 0; padding: 0; }
  html, body { width: 801px; height: 1200px; overflow: hidden; background: var(--bg); }
  .poster { position: relative; width: 801px; height: 1200px; font-family: "Roboto", Arial, sans-serif; }
  .arcs { position: absolute; inset: 0; }
  .column { position: absolute; left: 171px; width: 463px; top: 0; height: 1200px; background: var(--column); }
  .band {
    position: absolute; display: flex; align-items: center; justify-content: center;
    background: linear-gradient(90deg, var(--band-from), var(--band-to));
    color: #fff; font-family: "Montserrat", Arial, sans-serif; font-weight: 800;
    font-size: 42px; letter-spacing: 1px; white-space: nowrap;
  }
  .band--accountable { left: 171px; width: 463px; top: 0; height: 77px; }
  .band--life { left: 206px; width: 428px; top: 552px; height: 96px; font-size: 42px; }
  .band--victim { left: 171px; width: 463px; top: 1106px; height: 94px; }
  .ladder { position: absolute; left: 171px; width: 463px; list-style: none; }
  .ladder--upper { top: 103px; }
  .ladder--lower { top: 648px; }
  .rung { position: relative; height: 91px; border-top: 2px solid var(--column-dark); list-style: none; }
  .ladder--lower .rung { height: 91.6px; }
  .rung__step {
    position: absolute; left: 0; top: 0; bottom: 0; width: 80px; background: var(--step);
    display: flex; align-items: center; justify-content: flex-end; padding-right: 4px;
    font-family: "Montserrat", Arial, sans-serif; font-weight: 800; font-size: 86px;
    color: var(--step-number); overflow: hidden; line-height: 1;
  }
  .rung__text { position: absolute; left: 138px; top: 22px; white-space: nowrap; }
  .rung__label { font-weight: 900; font-size: 16px; letter-spacing: 0.8px; text-transform: uppercase; }
  .rung__quote { margin-top: 6px; font-size: 15px; color: var(--quote); }
  .is-yellow { color: var(--yellow); }
  .is-magenta { color: var(--magenta); }
  .is-green { color: var(--green); }
  .is-blue { color: var(--blue); }
  .is-purple { color: var(--purple); }
</style>
</head>
<body>
<main class="poster">
  <svg class="arcs" width="801" height="1200" viewBox="0 0 801 1200" aria-hidden="true">
    <path d="M175 40 C 10 70, -5 540, 210 570" fill="none" stroke="var(--arc)" stroke-width="9"/>
    <path d="M630 600 C 810 640, 810 1130, 630 1152" fill="none" stroke="var(--arc-light)" stroke-width="9"/>
  </svg>

  <div class="column"></div>

  <h1 class="band band--accountable">ACCOUNTABLE</h1>

  <ul class="ladder ladder--upper">
    <li class="rung"><span class="rung__step">5</span>
      <div class="rung__text"><p class="rung__label is-yellow">Gets on with it</p><p class="rung__quote">&ldquo;O.K., let&rsquo;s do it&rdquo;</p></div></li>
    <li class="rung"><span class="rung__step">4</span>
      <div class="rung__text"><p class="rung__label is-magenta">Finds solution</p><p class="rung__quote">&ldquo;What can I do?&rdquo;</p></div></li>
    <li class="rung"><span class="rung__step">3</span>
      <div class="rung__text"><p class="rung__label is-green">Owns it</p><p class="rung__quote">&ldquo;If it&rsquo;s to be, it&rsquo;s up to me&rdquo;</p></div></li>
    <li class="rung"><span class="rung__step">2</span>
      <div class="rung__text"><p class="rung__label is-blue">Acknowledges reality</p><p class="rung__quote">&ldquo;This is the way it is&rdquo;</p></div></li>
    <li class="rung"><span class="rung__step">1</span>
      <div class="rung__text"><p class="rung__label is-purple">Seeks reality</p><p class="rung__quote">&ldquo;What&rsquo;s happening&rdquo;</p></div></li>
  </ul>

  <h2 class="band band--life">LIFE HAPPENS</h2>

  <ul class="ladder ladder--lower">
    <li class="rung"><span class="rung__step">5</span>
      <div class="rung__text"><p class="rung__label is-yellow">Avoids reality</p><p class="rung__quote">&ldquo;Asks no questions&rdquo;</p></div></li>
    <li class="rung"><span class="rung__step">4</span>
      <div class="rung__text"><p class="rung__label is-magenta">Fights reality</p><p class="rung__quote">&ldquo;That&rsquo;s not how I see it&rdquo;</p></div></li>
    <li class="rung"><span class="rung__step">3</span>
      <div class="rung__text"><p class="rung__label is-green">Blames</p><p class="rung__quote">&ldquo;If everyone would just do their job&rdquo;</p></div></li>
    <li class="rung"><span class="rung__step">2</span>
      <div class="rung__text"><p class="rung__label is-blue">Personal excuses</p><p class="rung__quote">&ldquo;It&rsquo;s not my job&rdquo;</p></div></li>
    <li class="rung"><span class="rung__step">1</span>
      <div class="rung__text"><p class="rung__label is-purple">Waits hopes</p><p class="rung__quote">&ldquo;If it was meant to be, it&rsquo;ll happen&rdquo;</p></div></li>
  </ul>

  <h2 class="band band--victim">VICTIM</h2>
</main>
</body>
</html>
```